Design for Outdoor Sign/Banner to be used at Markets/Pop Up Events

We are a small boutique nursery based in Warner, Qld specialising in Platycerium species. We propagate, grow and sell the 18 different species of Platycerium. All of our Platyceriums are grown in shade houses on site and are hardened in natural conditions. We would like to see designs that use the colour green. I will attach our Company Logo and also the Stubbie Cooler Design that a designer created through Motif Harbour. Banner size would be approx 2 metres wide, 1 metre high.

```html
<!DOCTYPE html>
<html lang="en">
<head>
<meta charset="utf-8">
<title>Platycerium Grower – Market Banner</title>
<link rel="stylesheet" href="https://fonts.googleapis.com/css2?family=Oswald:wght@600&family=Itim&display=swap">
<style>
  :root {
    --stage: #dcdddc;
    --banner-green: #04620b;
    --ink-white: #ffffff;
    --shadow-dark: rgba(0, 30, 0, 0.75);
    --plant-light: #8cc45a;
    --plant-deep: #3f7f2a;
  }
  html, body {
    margin: 0;
    padding: 0;
    width: 1200px;
    height: 850px;
    overflow: hidden;
    background: var(--stage);
  }
  .banner {
    position: absolute;
    left: 40px;
    top: 145px;
    width: 1120px;
    height: 560px;
    background: var(--banner-green);
    overflow: hidden;
  }
  .brand {
    position: absolute;
    left: 37px;
    top: 62px;
    width: 207px;
    height: 230px;
    display: flex;
    align-items: center;
    justify-content: center;
    gap: 12px;
  }
  .brand-mark {
    width: 16px;
    height: 16px;
    background: var(--ink-white);
    flex: none;
  }
  .brand-name {
    font-family: "Oswald", sans-serif;
    font-weight: 600;
    color: var(--ink-white);
    font-size: 44px;
    line-height: 1.05;
    text-align: left;
    white-space: nowrap;
    margin: 0;
  }
  .plant-photo {
    position: absolute;
    left: 850px;
    top: 61px;
    width: 258px;
    height: 258px;
    border-radius: 40% 40% 12px 12px;
    background: radial-gradient(ellipse at 55% 35%, var(--plant-light), var(--plant-deep) 75%, rgba(4, 98, 11, 0) 100%);
  }
  .headline {
    position: absolute;
    z-index: 1;
    left: 283px;
    top: 78px;
    width: 560px;
    margin: 0;
    font-family: "Oswald", sans-serif;
    font-weight: 600;
    color: var(--ink-white);
    text-align: center;
    text-shadow: 4px 5px 6px var(--shadow-dark);
    white-space: nowrap;
  }
  .headline-line {
    display: block;
    font-size: 94px;
    letter-spacing: 2px;
    line-height: 110px;
  }
  .divider {
    position: absolute;
    left: 0;
    top: 365px;
    width: 1118px;
    height: 14px;
    background: var(--ink-white);
  }
  .tagline {
    position: absolute;
    left: 0;
    top: 408px;
    width: 1120px;
    margin: 0;
    font-family: "Itim", sans-serif;
    font-size: 118px;
    line-height: 1;
    color: var(--ink-white);
    text-align: center;
    white-space: nowrap;
    text-shadow: 4px 5px 6px var(--shadow-dark);
  }
</style>
</head>
<body>
  <main class="banner">
    <div class="brand">
      <span class="brand-mark"></span>
      <p class="brand-name">BRACKEN<br>HILL</p>
    </div>
    <div class="plant-photo" role="img" aria-label="Staghorn fern growing in a white square pot"></div>
    <h1 class="headline">
      <span class="headline-line">PLATYCERIUM</span>
      <span class="headline-line">GROWER</span>
    </h1>
    <div class="divider"></div>
    <p class="tagline">18 different species</p>
  </main>
</body>
</html>
```